Web Design Project

To Create new charity website currently (www.morvalenhope.org)
Please request for full requirements in PDF format via email.
dilan.perow@morvalenhope.org cc: dperow_dp@quillmail.com.au

Im unable to load the project details on this page through add files feature. Please ensure you understand the requirments and use www.brightkinfold.com as a good reference. or guide.

Create Users , Registers a Child for Sponsor, Search for a Child to sponsor byCountry, Town, Age group, Gender, Race, Religion days waiting

Donate, Shop from MHG Store, Events, what we do, Get Involved Category, gallery, Upcoming events.

-Main Focus on Child Sponsor
Online Registeration request for Child Support to MHG Team allow document upload by the registering person.

MHG Team reviews the request checking and verifying all the details including documents submitted
(this will be published after being approved by MHG Committee. once approved then MHG Publishes the details for sponsors

There should be section where highlights are uniquely identified. such as upcoming event or shows, Appeal for Cyclone or Flood Relief or Medical Assistance.
May be scrolling text or something similar.
#Manage community fundraisers and display their information, performance etc. Automated online letter on thanks, support and reminders such as Bdays and payment renewals.

#The addition should consist of online database which tracks upcoming fundraising events, fundraisers, team and donations. Photo and events gallery. Sponsors,
Online ecards, registerations of sponsor, members, volunteers and all internet users who want to receive regular updates.

Registeration database to create users by category (may be)
sponsor, looking for sponsors, volunteers, members, donors, others etc. create registeration and capture info in database
name , dob, gender, country, email add, phone
registeration needs to be verified by email confirmation link send back to email add supplied for verification

1. A fundraising home page with an attractive layout that displays an overview of fundraising events, teams and individuals. This information could be organized by event location, date etc.

2. Event Home page for each fundraising event. We need to tap into our e-commerse setup to allow us to include a) a gauge of how much has been raised so far, b) a list of recent donors and their messages c) a way for people to donate directly to the fundraiser or team member, and d) some sort of blog that the fundraiser themselves can update with pictures and information.

admin page.
number of visits made to web site.
registered members
After its launched it wil be manages by our members,

reference to www.brightkinfold.com/ our members have liked this very much
and also get involved from and shop from http://tarwickaid.org.au/ to get more ideas and use only as a reference to bring user friendliness and efficient elegant look and ease of use to users.

The final product modern and inspire people to get involved and fundraise. and provide online donations and gifts and also shopping benefits through our web site to get discounts to all internet shoppers

Administration Page.

////////////////////////////////////////////////////////////////////////////////////////////
Registeration is required for
for sponsors, Child looking for sponsor, Shopping Donors, Members Volunteers etc

Username / Password
User details name
Name (s) First, Last Middle Address, Suburb/Town, Country, Post Code, +
Land Line: Country Code/Area Code/#
Mobile: Country Code/Number
Password Reset Method via email or secret Q/A at least 2.

Other functions as a registered users of MHG to provide
Account Summary
My Sponsorship
Additional Givings
Write my Child/Sponsor
make a Payment
Account Settings
Payment Options
My Activity
Questions.

I need the Unique identifyiny feature for upcoming event appeal for something that attracts peoples attention.

May be a bold scrolling text such : Morvalen Hope Group has lauched KORALI STORM DRIVE 2013, or Priyanka Medical Assistance Appeal and once a person clicks on the scrolling text get the full details of the appeal and what needs to be done to support. Should not be limited to only 1 appeal but may be upto 512 Characters or some better ways of presenting. eg may be there is appeal, fund raiser, medical assistance etc.

Childs Sponsor and other activity
Register a Child
Search for a Child
Sponsor a Child

Persons willing to register for a chile Online Registration request for Child Support

Name, middle Surname,
Age: 9 (calculated Automatically from DOB)
• Birthday: February 15, 2004 (Drop Down Box_
• Gender: Female (Radio button)
• Country: (select from List)
• Town/City: (select from List)
• Suburb/Village: (User Entry If Doesn’t Exist) Or better approach
• Ethnicity/Race: (User Enter if doesn’t exist) Or better approach
• Religion: (User Enters If doesn’t exist) Or better approach
• Photo
• Child ID: Automatically Generated by System
o Initial Registeration Child ID will be prefixed by letter z. eg z123456
o Once approved and published by MHG Administrator prefix z will be removed. Automatically
MHG Administrator should be able to edit update add or delete any information from maintenance Page or from the database.

o Calculate from date of publishing Child Waiting: 257 Days for a sponsor
o
• Allow Upload of supporting document Document (Any Format for verification)
• Allow upload of Photos (s) max of 3

Registeration MUST
All Person who are looking for Child to support or looking for sponsors or donations charity membership, Volunteers subscribing for new letters and events must register first, Social networking.

TO Register with MHG
Username, password min of 6 max 10, Firstname, Lastname, TownCity, Country, email:
Optional:
Phone: country code, area code number Mobile: Country Code, Mobile number
Every registered person should be able to see all HIS ACTIVITY donations and other details under his profile:

Administration Page
Easy Manageable Admin Page
All step by step guide of updating each and every page
Tools and software must be provided for managing the website.
Easy and efficient way of Managing Pictures Allow single multiple and all images in a folder to be uploaded in simple steps: Able to reset password if required.

Well Structured layout and defined layers links to each and every page. Home button to be available in all pages.

Reports
MHG Admin should be able to generate reports from database such as mysql if any other db used some simple queries or adhoc report to be generated
Eg: All sales in MHG Store by date cateogy amount total sales by country and town grouped by:

Upcoming Events
Allows easy and user friendly interface for updating the pages for upcoming events.
MHG Admin should be able to send email to all registered users with attachments such as news letters, request for support etc etc

Gallery
MHG Admin should be able to able select the default folder to use for Scrolling images
Eg: 1 week I would all sponsored childs folder to be used to scroll all images
2nd week I may default to all events pics
3rd I may select Diaster relief
Or I can use random pics from all folders under gallery
My folder structure for gallery may be like this. I will select where Im uploading photos and then

Gallery
Childs
Disaster
Events
Stores (Note Stores will also have scrolling images for all items listed for sale) and it has to have a tag and stock list or number of items available once it reaches 0 it should be labeled out of stock.

• Create Child ID Automatically and Photos to MHG Team allow document upload by the registering person.

manage community fundraisers and display their information, performance etc. Automated online letter of thanks, support and reminders payment renewals due day and 7 days before due date. Bdays

Additional info that may be useful but not necessary and if it can improve in way to make our web site more attractive and efficient.
During Registeration needs to be verified by email confirmation link send back to email add supplied for verification and the user gets registered

2. Events page for each category fundraising team event.
Sponsor a Child
Micro Enterprise
Social Events
Medical Assitance
Relief & Assistance
IT Projects
Special Projects

We need to tap into our e-commerse setup to allow us to include
a) a gauge of how much has been raised so far, b) a list of recent donors and their messages c) a way for people to donate directly to the fundraiser or team member, and d) some sort of blog that the MHG fundraiser Team Leader themselves can update with pictures and information.

Number of visits made to web site.
Marketing links/ Ads

Example: http://www.brightkinfold.com/
our members have liked this very much
and also
get involved from and shop from
http://tarwickaid.org.au/

Updates

Hi All

I need to complete this project asap. may be in next 4 to 6 weeks maximum

so please submit you design overview, features functionality

thanks

Dilan

                                       

Project Details/Requirements

To Create new charity website currently (www.morvalenhope.org) reference www.brightkinfold.com

 

Create login (for sponsors, Child looking for sponsor, Shopping Donors, Members Volunteers etc

               Username / Password

               User details name

                              Name (s) First, Last Middle Address, Suburb/Town, Country, Post Code,  +

 

Other functions as a registered users of MHG  to provide

Account Summary

My Sponsorship

Additional Givings

Write my Child/Sponsor

make a Payment

Account Settings

Payment Options

My Activity

Questions.

 

Reference to snapshot below

 

 

 

 

 

Change the background colour. Need to have a good search feature for the child. Refer to www.brightkinfold.org web site as a guide pretty much very similar features I need. Also

 

 

               Register a Child

               Search for a Child

               Sponsor a Child

 

 

<!-[if !supportLists]->·        <!-[endif]->Online Registration request for Child Support

<!-[if !supportLists]->·        <!-[endif]->Age: 9  (calculated Automatically from DOB)

<!-[if !supportLists]->·        <!-[endif]->Birthday: February 15, 2004  (Drop Down Box_

<!-[if !supportLists]->·        <!-[endif]->Gender: Female (Radio button)

<!-[if !supportLists]->·        <!-[endif]->Country: (select from List)

<!-[if !supportLists]->·        <!-[endif]->Town/City: (select from List)

<!-[if !supportLists]->·        <!-[endif]->Suburb/Village: (User Entry If Doesn’t Exist) Or better approach

<!-[if !supportLists]->·        <!-[endif]->Ethnicity/Race: (User Enter if doesn’t exist) Or better approach

<!-[if !supportLists]->·        <!-[endif]->Religion: (User Enters If doesn’t exist) Or better approach

<!-[if !supportLists]->·        <!-[endif]->Photo

<!-[if !supportLists]->·        <!-[endif]->Child ID: Automatically Generated by System

<!-[if !supportLists]->o   <!-[endif]->Initial Registeration Child ID will be prefixed by letter z. eg z123456

<!-[if !supportLists]->o   <!-[endif]->Once approved and published by MHG Administrator prefix z will be removed. Automatically

<!-[if !supportLists]->·        <!-[endif]-> 

<!-[if !supportLists]->o   <!-[endif]->Calculate from date of publishing Child Waiting: 257 Days for a sponsor

<!-[if !supportLists]->o   <!-[endif]-> 

<!-[if !supportLists]->·        <!-[endif]->Allow Upload of supporting document Document (Any Format for verification)

<!-[if !supportLists]->·        <!-[endif]->Allow upload of Photos (s) max of 3

 

Registeration MUST

 

TO Register with MHG

Optional:

Phone: country code, area code number  Mobile: Country Code, Mobile number

 

 

 

            

                           

Administration Page

Easy and efficient way of Managing Pictures Allow single multiple and all images in a folder to be uploaded in simple steps

 

              

Reports

 

Upcoming Events

 

Gallery

 

               Gallery

                              Childs

                              Disaster

                              Events

                              Stores  (Note Stores will also have scrolling images for all items listed for sale) and it has to have a tag and stock list or number of items available once it reaches 0 it should be labeled out of stock.

                             

 

 

<!-[if !supportLists]->·        <!-[endif]->Create Child ID Automatically and Photos  to MHG Team allow document    upload by the registering person.

<!-[if !vml]-><!-[endif]->

         MHG Team reviews the request checking and verifying all the details including    documents submitted

        

        

manage community fundraisers and display their information, performance etc. Automated online letter of thanks, support and reminders payment renewals due day and 7 days before due date.  Bdays

 

 

 

Sponsor a Child

                              Micro Enterprise

                              Social Events

                              Medical Assitance

                              Relief & Assistance

                              IT Projects

                              Special Projects

 

                             

 

Marketing links/ Ads

 

 

 

 

and also

http://tarwickaid.org.au/

 

 

 

 

                                   

Target Market(s)

get and attract as many charity supporters as possible

Industry/Entity Type

Internet

Requirements
Must have
• Refer to attached documents
Users manual or step by step guide on how to manage and update web pages.
Nice to have
• nice catchy looks and layout
Reporting online options

```html
<!DOCTYPE html>
<html lang="en">
<head>
<meta charset="utf-8">
<title>Morvalen Hope Australia – Sponsor a Child</title>
<link rel="stylesheet" href="https://fonts.googleapis.com/css2?family=Exo+2:wght@500;600;700&family=Source+Sans+3:wght@400;600&display=swap">
<style>
:root{
  --royal:#0a2fc4;
  --royal-deep:#061a8a;
  --navy:#0b2a7a;
  --heading:#0b3aa8;
  --link:#0a3b9c;
  --button:#0d2a72;
  --panel:#ecebec;
  --ink:#1c1c1c;
  --footer:#0c2a8c;
  --footer-line:#2a47a6;
  --badge:#c4c4c4;
  --white:#fff;
}
*{box-sizing:border-box;margin:0;padding:0}
html,body{width:1200px;height:2290px;overflow:hidden}
body{
  position:relative;
  font-family:"Source Sans 3",Arial,sans-serif;
  color:var(--ink);
  background:radial-gradient(ellipse at 50% 20%,#1a4af0 0%,var(--royal) 35%,var(--royal-deep) 100%);
}
a{color:inherit;text-decoration:none}
.abs{position:absolute}

.flag-strip{left:0;top:0;width:1200px;height:9px;
  background:linear-gradient(90deg,#3a6,#c33,#fff,#23a,#fc3,#3a6,#c33,#fff,#23a,#fc3,#3a6,#c33,#fff,#23a,#fc3,#c33)}
.brand{left:46px;top:48px;display:flex;align-items:center;gap:12px}
.brand-mark{width:30px;height:30px;background:var(--white)}
.brand-name{font-family:"Exo 2",Arial,sans-serif;font-weight:600;color:var(--white);font-size:22px;line-height:1.15;letter-spacing:1px}
.brand-name span{display:block;font-size:15px;letter-spacing:10px}

.account-links{left:873px;top:32px;width:275px;height:36px;background:var(--royal-deep);
  border-radius:3px;display:flex;align-items:center;justify-content:center;gap:12px;
  font-size:13px;color:var(--white);font-weight:600}
.account-links i{font-style:normal;opacity:.7}
.site-search{left:875px;top:110px;width:263px;height:30px;background:var(--white);
  display:flex;align-items:center;padding:0 10px;font-size:12px;color:#888;justify-content:space-between}

.main-nav{left:38px;top:165px;width:1107px;height:64px;
  background:linear-gradient(180deg,#1c52e6,#0f36c0);display:flex;align-items:center;
  padding-left:46px;font-size:20px;color:var(--white)}
.main-nav a{padding:0 21px;border-right:1px solid rgba(255,255,255,.3);line-height:30px}
.main-nav a:first-child{padding-left:0}
.main-nav a:last-child{border-right:0}

.hero{left:34px;top:244px;width:1114px;height:367px;background:var(--white);
  box-shadow:0 0 14px rgba(255,255,255,.5)}
.hero-photo{left:53px;top:260px;width:717px;height:343px;
  background:linear-gradient(160deg,#6a4a3a,#b48a6c 40%,#5a6f8a 75%,#8a5a44)}
.slider-dots{left:696px;top:584px;display:flex;gap:7px}
.slider-dots span{width:10px;height:10px;background:var(--white)}
.child-search{left:785px;top:256px;width:345px;height:347px;background:var(--panel);
  border:3px solid #d0d0d0;padding:20px 22px}
.child-search h2{font-family:"Exo 2",Arial,sans-serif;font-weight:500;font-size:24px;color:var(--navy);margin-bottom:18px}
.child-search label{display:block;font-size:14px;color:var(--navy);font-weight:600;margin-bottom:4px}
.field{height:32px;background:var(--white);border:1px solid #ccc;font-size:12px;color:#777;
  padding:0 10px;display:flex;align-items:center;margin-bottom:18px}
.range{position:relative;height:16px;margin:6px 0 28px}
.range::before{content:"";position:absolute;left:0;right:0;top:6px;height:4px;background:var(--navy)}
.range span{position:absolute;top:1px;width:14px;height:14px;border-radius:50%;background:#7fb0f2}
.btn{display:inline-flex;align-items:center;justify-content:center;background:var(--button);
  color:var(--white);font-size:16px;border-radius:2px}
.child-search .btn{width:125px;height:34px}

.content{left:35px;top:632px;width:1112px;height:1315px;background:var(--white)}
.section-title{font-family:"Exo 2",Arial,sans-serif;font-weight:700;color:var(--heading);letter-spacing:.5px}
.sponsor-title{left:61px;top:660px;font-size:27px}
.sponsor-sub{left:62px;top:698px;font-size:14px;color:var(--heading);font-weight:600}

.child-card{top:733px;width:255px;height:369px;
  background:linear-gradient(180deg,#e2e2e2,#fafafa 50%,#e2e2e2);text-align:center;font-size:15px}
.child-photo{margin:16px auto 0;width:211px;height:179px;border:4px solid var(--white);
  box-shadow:0 1px 4px rgba(0,0,0,.3)}
.child-card p{margin-top:8px;line-height:20px}
.child-card p:first-of-type{margin-top:14px}
.child-card .btn{margin-top:10px;width:125px;height:34px;font-size:16px}

.news-title{left:61px;top:1138px;font-size:19px}
.news-item{top:1178px;width:240px;font-size:11.5px;line-height:17px;color:var(--ink)}
.news-item h3{font-weight:400;font-size:16px;margin-bottom:8px}
.news-item p{height:74px}
.more{color:var(--link);font-size:14px;display:block;margin-top:6px}

.divider{left:61px;top:1344px;width:1058px;height:1px;background:#d5d5d5}

.events-title{left:61px;top:1367px;font-size:19px}
.event{left:63px;width:740px;display:flex;gap:20px}
.event-thumb{flex:0 0 186px;height:134px;border:3px solid var(--white);box-shadow:0 1px 5px rgba(0,0,0,.35)}
.event h3{font-weight:400;font-size:17px;color:var(--link);margin:4px 0 8px}
.event p{font-size:11.5px;line-height:17px;margin-bottom:4px}

.featured-title{left:834px;top:1367px;font-size:19px}
.partner{background:var(--badge);border-radius:4px}

.other-title{left:845px;top:1683px;font-size:19px}
.other-list{left:847px;top:1720px;list-style:none;font-size:12.5px}
.other-list li{height:25px;display:flex;align-items:center;gap:8px}

.share-bar{left:35px;top:1947px;width:1112px;height:61px;background:#f1f1f1;
  display:flex;align-items:center;padding-left:34px;gap:28px;font-size:13.5px}
.social{left:977px;top:1962px;display:flex;gap:12px}
.social span{width:35px;height:35px;border-radius:50%;background:linear-gradient(#f3f3f3,#c8c8c8);border:1px solid #aaa}

.site-footer{left:0;top:2008px;width:1200px;height:282px;background:var(--footer)}
.footer-col{top:2038px;list-style:none;font-size:13.5px;color:var(--white)}
.footer-col li{height:31px;line-height:31px;border-bottom:1px solid var(--footer-line);width:110px}
.footer-col li:last-child{border-bottom:0}
.mission{left:676px;top:2023px;width:456px;height:184px;background:#0a2379;padding:14px 24px;color:var(--white)}
.mission h3{font-weight:400;font-size:18.5px;line-height:25px;margin-bottom:8px}
.mission p{font-size:12px;line-height:19px;color:#e4e8ff}
.mission a{display:block;margin-top:8px;font-size:13px}
.copyright{left:74px;top:2243px;font-size:11.5px;color:#dfe4ff}
</style>
</head>
<body>
<div class="abs flag-strip"></div>

<header>
  <a class="abs brand" href="#"><span class="brand-mark"></span><span class="brand-name">MORVALEN HOPE<span>AUSTRALIA</span></span></a>
  <nav class="abs account-links"><a href="#">My Account</a><i>|</i><a href="#">My Cart</a><i>|</i><a href="#">Contact Us</a></nav>
  <div class="abs site-search"><span>Enter keyword</span>
    <svg width="16" height="16" viewBox="0 0 16 16"><circle cx="6.5" cy="6.5" r="4.5" fill="none" stroke="#1a4fd0" stroke-width="2"/><line x1="10" y1="10" x2="15" y2="15" stroke="#1a4fd0" stroke-width="2.5"/></svg>
  </div>
  <nav class="abs main-nav">
    <a href="#">home</a><a href="#">Sponsor a Child</a><a href="#">Gallery</a><a href="#">About Us</a><a href="#">Contact</a><a href="#">Events</a><a href="#">News</a><a href="#">Spotlight</a>
  </nav>
</header>

<section>
  <div class="abs hero"></div>
  <div class="abs hero-photo" role="img" aria-label="Photo of a group of children sitting together on the floor"></div>
  <div class="abs slider-dots"><span></span><span></span><span></span><span></span></div>
  <form class="abs child-search">
    <h2>Search for a Child</h2>
    <label>Where in The World</label><div class="field">city/state name goes here</div>
    <label>Gender</label><div class="field">male/female here</div>
    <label>Age Range:</label>
    <div class="range"><span style="left:14px"></span><span style="left:244px"></span></div>
    <span class="btn">Search Now</span>
  </form>
</section>

<main>
  <div class="abs content"></div>
  <h2 class="abs section-title sponsor-title">SPONSOR A CHILD TODAY</h2>
  <p class="abs sponsor-sub">Make an eternal difference in the life of a child in need. Sponsor a child today!</p>

  <article class="abs child-card" style="left:56px"><div class="child-photo" role="img" aria-label="Portrait photo of a smiling child" style="background:linear-gradient(150deg,#4a3a30,#c89878 55%,#6a5040)"></div><p>Name of Child</p><p>Country or place name here</p><p>11/03/1999</p><span class="btn">SPONSOR ME</span></article>
  <article class="abs child-card" style="left:328px"><div class="child-photo" role="img" aria-label="Portrait photo of a child" style="background:linear-gradient(150deg,#2a1a14,#a87458 55%,#3a241a)"></div><p>Name of Child</p><p>Country or place name here</p><p>11/03/1999</p><span class="btn">SPONSOR ME</span></article>
  <article class="abs child-card" style="left:599px"><div class="child-photo" role="img" aria-label="Portrait photo of a toddler in a red hat" style="background:linear-gradient(170deg,#c8202a,#d8a88a 45%,#e8e8e8)"></div><p>Name of Child</p><p>Country or place name here</p><p>11/03/1999</p><span class="btn">SPONSOR ME</span></article>
  <article class="abs child-card" style="left:869px"><div class="child-photo" role="img" aria-label="Portrait photo of a smiling young girl" style="background:linear-gradient(150deg,#5a4a3a,#8a6448 50%,#b0a030)"></div><p>Name of Child</p><p>Country or place name here</p><p>11/03/1999</p><span class="btn">SPONSOR ME</span></article>

  <h2 class="abs section-title news-title">LATEST NEWS</h2>
  <article class="abs news-item" style="left:63px"><h3>Fiji Flood Relief Appeal</h3><p>Morvalen Hope Group - Fiji Flood Relief Appeal Flood victims lost stationary bought for school children and bookshops their stock - school term has already started....</p><a class="more" href="#">learn more..</a></article>
  <article class="abs news-item" style="left:341px"><h3>Morvalen Hope Fiji Flood Appeal</h3><p>Morvalen Hope Australia (MHG), in conjunction with its global sister charities in USA, Canada, New Zealand &amp; Fiji, are requesting your kind support in collecting over 40,000</p><a class="more" href="#">learn more..</a></article>
  <article class="abs news-item" style="left:620px"><h3>Tavelu Nursing Station</h3><p>Morvalen Hope Australia supplies 2 x 2000 litres water tank to assist both the medical institutions to have abundance of wholesome water to run the day-to-day operation.</p><a class="more" href="#">learn more..</a></article>
  <article class="abs news-item" style="left:883px"><h3>Celebrating 10 Years of Giving</h3><p>Morvalen Hope Australia presents the biggest party aboard luxurious Lady Maren....... Tickets on sale now. All proceeds will go to under priviledged children of Fiji.</p><a class="more" href="#">learn more..</a></article>

  <div class="abs divider"></div>

  <h2 class="abs section-title events-title">UPCOMING EVENTS</h2>
  <article class="abs event" style="top:1413px"><div class="event-thumb" role="img" aria-label="Photo of a volunteer with a group of children" style="background:linear-gradient(140deg,#e8e0d8,#5a3a2a 50%,#b0a090)"></div><div><h3>Morvalen Hope Fiji Flood Relief Appeal</h3><p>Morvalen Hope Group - Fiji Flood Relief Appeal Flood victims lost stationary bought for school children and bookshops their stock - school term has already started.....</p><p>Larkbay eSolutions is a web service company, offering a wide range of services which range from designing and development, that is covering</p><a class="more" href="#">learn more..</a></div></article>
  <article class="abs event" style="top:1582px"><div class="event-thumb" role="img" aria-label="Photo of a group of children and adults at an event" style="background:linear-gradient(140deg,#6a5a50,#b83a3a 45%,#d8c8c0)"></div><div><h3>Morvalen Hope Fiji Flood Relief Appeal</h3><p>Morvalen Hope Group - Fiji Flood Relief Appeal Flood victims lost stationary bought for school children and bookshops their stock - school term has already started.....</p><p>Larkbay eSolutions is a web service company, offering a wide range of services which range from designing and development, that is covering</p><a class="more" href="#">learn more..</a></div></article>
  <article class="abs event" style="top:1751px"><div class="event-thumb" role="img" aria-label="Photo of a donation being handed over at a ceremony" style="background:linear-gradient(140deg,#8a6030,#d8b078 45%,#3a2a20)"></div><div><h3>Morvalen Hope Fiji Flood Relief Appeal</h3><p>Morvalen Hope Group - Fiji Flood Relief Appeal Flood victims lost stationary bought for school children and bookshops their stock - school term has already started.....</p><p>Larkbay eSolutions is a web service company, offering a wide range of services which range from designing and development, that is covering</p><a class="more" href="#">learn more..</a></div></article>

  <h2 class="abs section-title featured-title">FEATURED ON</h2>
  <div class="abs partner" style="left:840px;top:1417px;width:96px;height:57px"></div>
  <div class="abs partner" style="left:960px;top:1432px;width:146px;height:36px;border-radius:18px"></div>
  <div class="abs partner" style="left:840px;top:1519px;width:95px;height:32px;border-radius:16px"></div>
  <div class="abs partner" style="left:966px;top:1519px;width:126px;height:34px"></div>
  <div class="abs partner" style="left:843px;top:1588px;width:104px;height:48px;border-radius:24px"></div>
  <div class="abs partner" style="left:989px;top:1600px;width:92px;height:28px;border-radius:3px"></div>

  <h2 class="abs section-title other-title">OTHER NEWS SITES</h2>
  <ul class="abs other-list">
    <li><svg width="14" height="12" viewBox="0 0 14 12"><path d="M1 6l4 4 8-9" fill="none" stroke="#0b2a7a" stroke-width="2.6"/></svg>2009 Flood Relief</li>
    <li><svg width="14" height="12" viewBox="0 0 14 12"><path d="M1 6l4 4 8-9" fill="none" stroke="#0b2a7a" stroke-width="2.6"/></svg>2009 Flood School donation</li>
    <li><svg width="14" height="12" viewBox="0 0 14 12"><path d="M1 6l4 4 8-9" fill="none" stroke="#0b2a7a" stroke-width="2.6"/></svg>Expatriate Fijians Help Fiji Temple</li>
    <li><svg width="14" height="12" viewBox="0 0 14 12"><path d="M1 6l4 4 8-9" fill="none" stroke="#0b2a7a" stroke-width="2.6"/></svg>Coral Times – Helping hand for the needy</li>
    <li><svg width="14" height="12" viewBox="0 0 14 12"><path d="M1 6l4 4 8-9" fill="none" stroke="#0b2a7a" stroke-width="2.6"/></svg>Orchestra performs to aid the needy</li>
    <li><svg width="14" height="12" viewBox="0 0 14 12"><path d="M1 6l4 4 8-9" fill="none" stroke="#0b2a7a" stroke-width="2.6"/></svg>School's water problem solved</li>
    <li><svg width="14" height="12" viewBox="0 0 14 12"><path d="M1 6l4 4 8-9" fill="none" stroke="#0b2a7a" stroke-width="2.6"/></svg>Talvira Supports Fiji Flood Appeal</li>
  </ul>
</main>

<div class="abs share-bar"><a href="#">Email a Friend</a><a href="#">Subscribe</a><a href="#">Bookmark &amp; Share</a><a href="#">Print This Page</a></div>
<div class="abs social"><span></span><span></span><span></span></div>

<footer>
  <div class="abs site-footer"></div>
  <ul class="abs footer-col" style="left:84px"><li>Home</li><li>Sponsor a Child</li><li>Donate Now</li><li>Latest News</li><li>Gallery</li></ul>
  <ul class="abs footer-col" style="left:228px"><li>About Us</li><li>Spotlight</li><li>Upcoming Events</li><li>Comments</li></ul>
  <ul class="abs footer-col" style="left:380px"><li>Blog</li><li>Contact Us</li><li>Other Sites</li><li>Login</li></ul>
  <ul class="abs footer-col" style="left:499px"><li>Blog</li><li>Contact Us</li><li>Other Sites</li><li>Login</li></ul>
  <aside class="abs mission">
    <h3>Sponsoring a Child is Just Part of Brightkinfold's Ministry to Children in Need</h3>
    <p>Sponsor a Child — At Brightkinfold we take a committed, long-term approach to fighting child poverty. Our Holistic Child Development Model is made up of four comprehensive programs investing in children from the beginning of their lives until they've reached adulthood</p>
    <a href="#">learn more..</a>
  </aside>
  <p class="abs copyright">© 2012 Company Name &nbsp;| &nbsp;All right reserved &nbsp;| &nbsp;Term &amp; Conditions</p>
</footer>
</body>
</html>
```